Corwin Crest Homes Needs Business Card Design

Looking for a unique modern business card to fit my new Logo.
Name: Marcus Corwin
Company: Corwin Crest Homes, LLC
Tag Line: Always Crafted Right
Email: corwincresthomes@mailnest.example
Phone: (555) 017-2846
Website: www.corwincresthomes.example
License: CORWICH462KX

```html
<!DOCTYPE html>
<html lang="en">
<head>
<meta charset="utf-8">
<title>Corwin Crest Homes — Business Card</title>
<link href="https://fonts.googleapis.com/css2?family=Montserrat:wght@400;500;600;700&display=swap" rel="stylesheet">
<style>
  :root {
    --brand-blue: #3598cc;
    --brand-blue-deep: #1f7fb8;
    --ink: #111111;
    --paper: #ffffff;
    --backdrop: #ececec;
  }
  * { box-sizing: border-box; margin: 0; padding: 0; }
  html, body {
    width: 900px; height: 1200px; overflow: hidden;
    background: var(--backdrop);
    font-family: "Montserrat", sans-serif;
  }
  .canvas { position: relative; width: 900px; height: 1200px; }
  .card {
    position: absolute; left: 70px; width: 760px; height: 436px;
    overflow: hidden;
  }
  .card-front { top: 139px; background: var(--brand-blue); }
  .card-back { top: 625px; background: var(--paper); }

  .front-wordmark {
    position: absolute; left: 0; right: 0; top: 260px;
    text-align: center;
    font-weight: 700; font-size: 34px; letter-spacing: 1px;
    color: var(--brand-blue-deep);
  }

  .back-brand {
    position: absolute; left: 46px; top: 86px;
    display: flex; align-items: center; gap: 12px;
  }
  .brand-square { width: 28px; height: 28px; background: var(--brand-blue); flex: none; }
  .brand-name {
    font-weight: 700; font-size: 21px; color: var(--ink); letter-spacing: 0.3px;
    white-space: nowrap;
  }

  .owner {
    position: absolute; right: 38px; top: 80px; text-align: right;
  }
  .owner-name {
    font-weight: 600; font-size: 27px; color: var(--brand-blue); letter-spacing: 1.5px;
    white-space: nowrap;
  }
  .owner-title { font-weight: 500; font-size: 16px; color: var(--ink); letter-spacing: 1px; margin-top: 2px; }

  .contact-list {
    position: absolute; left: 45px; top: 282px; list-style: none;
  }
  .contact-list li {
    display: flex; align-items: center; gap: 8px;
    font-size: 17px; font-weight: 500; color: var(--ink);
    height: 28px;
  }
  .contact-list .phone { letter-spacing: 2.5px; }
  .contact-list svg { width: 18px; height: 18px; flex: none; }
  .license {
    position: absolute; left: 45px; top: 380px;
    font-size: 17px; font-weight: 500; color: var(--ink); letter-spacing: 0.8px;
  }
  .license-label { color: var(--brand-blue); font-weight: 600; }

  .tagline {
    position: absolute; right: 0; top: 363px; width: 329px; height: 46px;
    background: var(--brand-blue); border-radius: 23px 0 0 23px;
    color: var(--paper); font-weight: 600; font-size: 19px; letter-spacing: 2px;
    display: flex; align-items: center; padding-left: 19px;
    white-space: nowrap;
  }
</style>
</head>
<body>
<main class="canvas">
  <section class="card card-front" aria-label="Card front">
    <div class="front-wordmark">CORWIN CREST HOMES</div>
  </section>

  <section class="card card-back" aria-label="Card back">
    <div class="back-brand">
      <span class="brand-square"></span>
      <span class="brand-name">CORWIN CREST HOMES</span>
    </div>

    <div class="owner">
      <div class="owner-name">MARCUS CORWIN</div>
      <div class="owner-title">Owner</div>
    </div>

    <ul class="contact-list">
      <li class="phone">
        <svg viewBox="0 0 24 24" aria-hidden="true"><path fill="#3598cc" d="M6.6 10.8a15.1 15.1 0 0 0 6.6 6.6l2.2-2.2c.3-.3.7-.4 1-.2 1.1.4 2.3.6 3.6.6.6 0 1 .4 1 1V20c0 .6-.4 1-1 1C10.6 21 3 13.4 3 4c0-.6.4-1 1-1h3.5c.6 0 1 .4 1 1 0 1.3.2 2.5.6 3.6.1.3 0 .7-.2 1z"/></svg>
        (555) 017-2846
      </li>
      <li>
        <svg viewBox="0 0 24 24" aria-hidden="true"><rect x="2" y="5" width="20" height="14" fill="#3598cc"/><path d="M2 5l10 8 10-8" fill="none" stroke="#fff" stroke-width="1.8"/></svg>
        corwincresthomes@mailnest.example
      </li>
      <li>
        <svg viewBox="0 0 24 24" aria-hidden="true"><g fill="none" stroke="#3598cc" stroke-width="1.8"><circle cx="12" cy="12" r="9"/><ellipse cx="12" cy="12" rx="4" ry="9"/><path d="M3 12h18M5 7h14M5 17h14"/></g></svg>
        www.corwincresthomes.example
      </li>
    </ul>

    <div class="license"><span class="license-label">License:</span> CORWICH462KX</div>

    <div class="tagline">ALWAYS CRAFTED RIGHT</div>
  </section>
</main>
</body>
</html>
```